Luxury Brand Real Estate For Sale sign

**Update** I've added some examples from the internet of other signs that have a look similar to what I would like to see. I do not want my personal name in the sign. And the word FOR SALE Does not need to be so large - it can be more subtle.
I want to create a Real Estate for sale sign for my company that will be used for luxury/higher end real estate listings. I’m sharing my business card as well as a logo with new teal color to show what we're moving towards: we’re using Teal, white, black and gold.
Hoping the sign is simple, sophisticated and eye catching.
The sign should be 24" wide by 30" tall including the company name: Harbor Crest Realty Group and our logo, office phone number 727-555-0148 and website www.hcrgexample.com the words "For Sale"
Optional to add this e-mail address info@hcrgexample.com to the sign
Target Market(s)
Luxury home buyers
Industry/Entity Type
Real Estate
Look and feel

```html
<!DOCTYPE html>
<html lang="en">
<head>
<meta charset="utf-8">
<title>Harbor Crest Realty Group – For Sale</title>
<link rel="stylesheet" href="https://fonts.googleapis.com/css2?family=Bebas+Neue&family=Montserrat:wght@600;700;800&display=swap">
<style>
  :root {
    --teal: #0e8380;
    --teal-sheen: #8fc5c3;
    --ink: #333132;
    --sky: #cfe5e6;
    --white: #ffffff;
  }
  html, body {
    margin: 0;
    padding: 0;
    width: 1198px;
    height: 1200px;
    overflow: hidden;
    background: var(--white);
  }
  .sign {
    display: block;
    width: 1198px;
    height: 1200px;
  }
  .brand-name {
    font-family: "Montserrat", sans-serif;
    font-weight: 700;
    fill: var(--ink);
  }
  .headline {
    font-family: "Bebas Neue", sans-serif;
    fill: var(--white);
  }
  .phone-number {
    font-family: "Montserrat", sans-serif;
    font-weight: 800;
    fill: var(--ink);
  }
  .website {
    font-family: "Montserrat", sans-serif;
    font-weight: 600;
    fill: var(--white);
  }
</style>
</head>
<body>
<svg class="sign" viewBox="0 0 1198 1200" xmlns="http://www.w3.org/2000/svg" aria-label="Harbor Crest Realty Group for sale sign">
  <defs>
    <linearGradient id="sky-fade" x1="0" y1="0" x2="0" y2="1">
      <stop offset="0" stop-color="var(--sky)"/>
      <stop offset="1" stop-color="var(--white)"/>
    </linearGradient>
    <linearGradient id="banner-sheen" x1="0" y1="1" x2="1" y2="0" gradientUnits="objectBoundingBox">
      <stop offset="0" stop-color="var(--teal)"/>
      <stop offset="0.42" stop-color="var(--teal)"/>
      <stop offset="0.78" stop-color="var(--teal-sheen)"/>
      <stop offset="0.78" stop-color="var(--teal)"/>
      <stop offset="1" stop-color="var(--teal)"/>
    </linearGradient>
    <linearGradient id="ribbon-sheen" x1="0" y1="1" x2="1" y2="0" gradientUnits="objectBoundingBox">
      <stop offset="0" stop-color="var(--teal)"/>
      <stop offset="0.15" stop-color="var(--teal)"/>
      <stop offset="0.36" stop-color="var(--teal-sheen)"/>
      <stop offset="0.36" stop-color="var(--teal)"/>
      <stop offset="1" stop-color="var(--teal)"/>
    </linearGradient>
  </defs>

  <!-- header -->
  <rect class="header-bg" x="0" y="0" width="1198" height="210" fill="url(#sky-fade)"/>
  <rect class="brand-square" x="102" y="106" width="128" height="128" fill="none" stroke="var(--teal)" stroke-width="5"/>
  <line class="brand-divider" x1="397" y1="82" x2="397" y2="248" stroke="var(--ink)" stroke-width="3"/>
  <text class="brand-name" x="430" y="171" font-size="62" textLength="667" lengthAdjust="spacingAndGlyphs">HARBOR CREST</text>
  <text class="brand-name" x="432" y="215" font-size="34" letter-spacing="20" textLength="445">REALTY GROUP</text>

  <!-- for sale banner -->
  <polygon class="headline-banner" points="94,413 1103,414 1037,654 148,655" fill="url(#banner-sheen)"/>
  <text class="headline" x="228" y="623" font-size="248" textLength="726" lengthAdjust="spacingAndGlyphs">FOR SALE</text>

  <!-- phone -->
  <g class="phone-icon" transform="translate(167 806)">
    <circle r="63" fill="none" stroke="var(--teal)" stroke-width="11"/>
    <path d="M-28 -30 l12 -6 l12 22 l-10 8 q6 18 24 26 l8 -10 l22 12 l-6 12 q-10 8 -26 2 q-32 -14 -42 -46 q-4 -14 6 -20z" fill="var(--teal)"/>
  </g>
  <text class="phone-number" x="268" y="856" font-size="140" textLength="784" lengthAdjust="spacingAndGlyphs">727-555-0148</text>

  <!-- footer -->
  <rect class="footer-stripe" x="0" y="1032" width="1198" height="18" fill="var(--teal)"/>
  <rect class="footer-base" x="0" y="1049" width="1198" height="151" fill="var(--ink)"/>
  <polygon class="web-ribbon" points="103,985 1095,985 1065,1096 127,1096" fill="url(#ribbon-sheen)"/>
  <g class="globe-icon" transform="translate(211 1042)" fill="none" stroke="var(--white)">
    <circle r="31" stroke-width="6"/>
    <circle r="18" stroke-width="3"/>
    <ellipse rx="8" ry="18" stroke-width="3"/>
    <line x1="-18" y1="0" x2="18" y2="0" stroke-width="3"/>
  </g>
  <text class="website" x="263" y="1071" font-size="68" textLength="758" lengthAdjust="spacingAndGlyphs">www.hcrgexample.com</text>
</svg>
</body>
</html>
```